Business Card for a Dental Office

The design should communicate integrity, quality and reliability. We also want the card look elegant, simple, but still stand out, different from the traditional-dental-office business card.

Business

```html
<!DOCTYPE html>
<html lang="en">
<head>
<meta charset="utf-8">
<title>Harlow Dental Studio – Business Card</title>
<link rel="stylesheet" href="https://fonts.googleapis.com/css2?family=Roboto+Condensed:wght@700&family=Open+Sans:wght@400;600&display=swap">
<style>
  :root {
    --bg: #e9e6e0;
    --card-black: #0c0c0c;
    --card-black-soft: #2a2a2a;
    --gold: #c3b22a;
    --gold-light: #d9c93d;
    --gold-dark: #a8981d;
    --white: #f4f4f4;
    --ink: #161616;
  }
  * { box-sizing: border-box; margin: 0; padding: 0; }
  html, body { width: 1200px; height: 1022px; overflow: hidden; }
  body {
    background: var(--bg);
    display: flex; align-items: center; justify-content: center;
    font-family: "Open Sans", sans-serif;
  }
  .card {
    position: relative;
    width: 1000px; height: 570px;
    border-radius: 26px;
    overflow: hidden;
    background: linear-gradient(160deg, var(--card-black) 0%, var(--card-black-soft) 55%, var(--card-black) 100%);
    box-shadow: 0 10px 30px rgba(0,0,0,.25);
  }
  .card-bands { position: absolute; inset: 0; }
  .brand {
    position: absolute; left: 90px; top: 100px;
    display: flex; align-items: center; gap: 26px;
  }
  .brand-mark {
    width: 92px; height: 92px;
    background: var(--gold);
    flex: none;
  }
  .brand-name {
    font-family: "Roboto Condensed", sans-serif;
    font-weight: 700;
    font-size: 62px; line-height: 1;
    color: var(--white);
    letter-spacing: .5px;
    text-transform: uppercase;
  }
  .brand-tagline {
    margin-top: 10px;
    font-family: "Open Sans", sans-serif;
    font-weight: 600;
    font-size: 24px; letter-spacing: 2px; line-height: 1.2;
    color: var(--white);
    text-transform: uppercase;
  }
  .brand-tagline .accent { color: var(--gold-light); }
  .person {
    position: absolute; right: 60px; top: 262px;
    text-align: right;
  }
  .person-name {
    font-family: "Roboto Condensed", sans-serif;
    font-weight: 700;
    font-size: 46px; line-height: 1;
    color: var(--ink);
    text-transform: uppercase;
  }
  .person-title {
    margin-top: 4px;
    font-size: 22px; letter-spacing: 2px;
    color: var(--gold-dark);
    text-transform: uppercase;
  }
  .contact {
    position: absolute; left: 90px; top: 418px;
    list-style: none;
    color: var(--ink);
    font-size: 24px; line-height: 34px;
  }
  .contact li { display: flex; align-items: center; gap: 16px; }
  .contact svg { width: 20px; height: 20px; flex: none; }
</style>
</head>
<body>
  <div class="card">
    <svg class="card-bands" width="1000" height="570" viewBox="0 0 1000 570" aria-hidden="true">
      <defs>
        <linearGradient id="gold-band" x1="0" y1="0" x2="0" y2="1">
          <stop offset="0" stop-color="#d6c538"/>
          <stop offset="1" stop-color="#b3a222"/>
        </linearGradient>
      </defs>
      <polygon points="0,382 560,382 625,372 1000,372 1000,384 630,384 570,394 0,394" fill="#f4f4f4"/>
      <polygon points="0,400 575,400 640,390 1000,390 1000,570 0,570" fill="url(#gold-band)"/>
      <polygon points="700,246 1000,246 1000,360 630,360 660,300" fill="#f4f4f4"/>
      <polygon points="690,240 1000,240 1000,246 700,246" fill="#0c0c0c"/>
    </svg>

    <div class="brand">
      <span class="brand-mark"></span>
      <div>
        <h1 class="brand-name">Harlow Dental Studio</h1>
        <p class="brand-tagline">Your smile is your <span class="accent">gift to others</span></p>
      </div>
    </div>

    <div class="person">
      <h2 class="person-name">Evan Marsh</h2>
      <p class="person-title">Director</p>
    </div>

    <ul class="contact">
      <li>
        <svg viewBox="0 0 20 20"><path d="M5 2l3 3-2 2c1 2.5 3 4.5 5.5 5.5l2-2 3 3-2 3C8 15.5 4.5 12 2 4z" fill="#f4f4f4"/></svg>
        +330 5512-0394
      </li>
      <li>
        <svg viewBox="0 0 20 20"><rect x="2" y="4" width="16" height="12" fill="none" stroke="#f4f4f4" stroke-width="2"/><path d="M2 4l8 7 8-7" fill="none" stroke="#f4f4f4" stroke-width="2"/></svg>
        info@harlowdentalstudio.com
      </li>
      <li>
        <svg viewBox="0 0 20 20"><circle cx="10" cy="10" r="8" fill="none" stroke="#f4f4f4" stroke-width="2"/><ellipse cx="10" cy="10" rx="3.5" ry="8" fill="none" stroke="#f4f4f4" stroke-width="1.5"/><path d="M2 10h16" stroke="#f4f4f4" stroke-width="1.5"/></svg>
        www.harlowdentalstudio.com
      </li>
    </ul>
  </div>
</body>
</html>
```